Football (soccer) board game app design

Hi,

We are a start up looking for a gameplay design for an app. It is a football trivia app that consists of four main screens; login/register, main navigation, gameplay, question.

OVERALL:
We want our app to be kept in a dark theme. Black or very dark gray is preferable, with a couple of nice colors to give it a stylish touch. We like flat designs, but are open for ideas within the general structure design. The logo can be used in the app, but feel free to improve it you feel you can. In the attached material we have tried to outline some of our ideas and other designs friends have helped us make.

LOGIN/REGISTER:
We want a simple login. Email, password, Linkora login and the possibility to register a new user. Live search check whether the email is valid and free, and there is also live validation of passwords. If this could be incorporated in the design it would be nice.

MAIN NAVIGATION:
In the main navigation screen we want it to be divided into tabs. A home, my games, my categories and a ranking tab. In the top bar it should be possible to search for categories as well as there should be a button to go to settings.

The Home tab
In the home tab we want a "Quick Play" button, and a list of featured categories. A category can be unlocked or locked, which should be illustrated somehow. When a category is tapped it should divide the block into a left and right tap area, where the user can choose to "Beat to unlock" or "Buy to unlock" if locked and "Practice" or "Challenge Friend" if already unlocked.

The My Games tab
In the my games tab, the current games should be divided into three lists. First "your turn", then "opponents turn" and finally "finished games".

The My Categories tab
This tab should include a list of categories, which the user have bought, but as of design it is fairly similar to the blocks in home tab. So not much different here.

The Ranking tab
Ranking should show a set of leaderboards; Today, This Week, This Month, etc. The row in a leaderboard should have teamname and a win percentage.

GAMEPLAY:
The gameplay is inspired by an old football (soccer) board game from the 1950's, and our gameplay consists of three core elements; a football (soccer) pitch, 11 players and a scoreboard.

The football (soccer) pitch
What we need is a pitch seen from behind the goal line. The important issue here, is the perspective, as we want 11 players on the field formed as a 4-3-3 formation, being 1 goalkeeper, 4 defenders, 3 midfielder and 3 strikers. They should all be touchable without overlap. In the other end we want a goal that should be touchable as well. The goal in the nearest end do not have to be visible. Due to the perspective of the field and the fact that players and goal should be touchable, of course give you the opportunity to play around with the proportions of both players and goal. We rather want a large goal being out of proportions, than a small goal with a tiny tap area. Around the field (sidelines and beside the goal) we would like advertising banners like seen on a real stadium.

The players
As mentioned we want 11 players in a 4-3-3 formation. The players should be attached to the board with springs as seen on some of the very old board games, where you could flick the player to pass the ball. This also means that we want the players to be placed in an indentation for the ball to fall into and it would be very cool if you could illustrate the player with the ball, as being pulled back to one of the sides, just enough to see the ball at his feet. The players should be large enough for a user to tap them, hence it would also be beneficial if they are not overlapping. For a start we would like to see the players in a blue shirt and white shorts (socks are not necessary as they are placed on a spring).

Scoreboard
On the scoreboard above the field, we need information such as the names of the two teams (could be FC Brightcrest and Red Oak Rovers), the score (2-1), minutes played (42), and which half (1st). We also want a progress bar that illustrates how many moves you have used ranging from 0-5. The scoreboard could be inspired from the ones seen around stadiums across the world, but feel free to improvise.

What We Are Looking for
We are looking for full PSD and AI files so we can use them to make minor changes like colors on shirts and shorts, colors on pitch, etc. We really want you to be innovative and inspire us, as we are not designers ourselves. In the attached files, we have tried to sketch out a design that covers our initial ideas. We are looking for a professional look, and having the players and field look like a real board game would just be awesome. A combination of the look from the realistic pitch with advertising banners around it, the idea of our spring-players and the initial thoughts of a design illustrated in our sketch, should help you along. Flat design, cartoonish or somewhere in between is up to you, we just want you to impress and make "wow"-feeling.

QUESTION:
The final screen should display a question with four possible answers. There should be a green/checkmark when correct answer, and a red/cross if incorrect.

That's all. We are looking very much forward to see your designs!
Updates

Hi all,

We have changed the terms of the contest to now have a guaranteed payment, and we are really looking forward to see your designs! Good luck.

/ Mattias and Anders

By request we have now uploaded an AI-file with the logo for you to play around with. We are looking forward to see your designs.

/ Mattias and Anders

Project Deadline Extended
Reason: Hi designers, We are really happy with the progress being made, and are looking forward to see some of the designs that are still work in progress. However the amount of designs received, has not reached our expectations yet. Therefore we are extending the deadline for seven more days, so designers, that are still working on their designs can continue their work without a stressing deadline in the horizon. Good luck to all of you. We are looking very much forward to see, what you are able to produce. Best regards, Mattias and Anders

Project Deadline Extended
Reason: Hi all, We still have a lot of designers in the competition , who are battling to finish their designs, therefore we have decided to extend the deadline once more. Good luck to all of you!

Target Market(s)

Football (soccer) fans

Industry/Entity Type

Advertising

```html
<!DOCTYPE html>
<html lang="en">
<head>
<meta charset="utf-8">
<title>Home</title>
<link rel="stylesheet" href="https://fonts.googleapis.com/css2?family=Montserrat:wght@500;600;700&family=Open+Sans:wght@400;600&display=swap">
<style>
  :root {
    --page-bg: #07121a;
    --page-glow: #0d2a38;
    --screen-bg: #0f1d29;
    --status-bg: #000000;
    --status-text: #e6e6e6;
    --tab-bg: #0d1a25;
    --tab-divider: #1d3244;
    --tab-track: #16293a;
    --tab-text: #f2f4f6;
    --accent: #1fc4ea;
    --button-top: #213a52;
    --button-bottom: #15293c;
    --button-border: #2d4a63;
    --row-top: #e6e7e9;
    --row-bottom: #b4b6b9;
    --row-divider: #c9cbce;
    --row-title: #1b1c1e;
    --row-meta: #55585c;
    --lock: #17324a;
  }
  * { box-sizing: border-box; margin: 0; padding: 0; }
  html, body { width: 1000px; height: 1200px; overflow: hidden; }
  body {
    background: radial-gradient(ellipse 520px 420px at 500px 140px, var(--page-glow), var(--page-bg) 75%);
    font-family: "Open Sans", sans-serif;
    position: relative;
  }
  .app-screen {
    position: absolute; left: 260px; top: 163px;
    width: 480px; height: 854px;
    background: var(--screen-bg);
  }
  .status-bar {
    height: 31px; background: var(--status-bg);
    display: flex; align-items: center; justify-content: space-between;
    padding: 0 6px; color: var(--status-text);
  }
  .status-carrier {
    display: flex; align-items: center; gap: 4px;
    font-family: "Montserrat", sans-serif; font-weight: 700; font-size: 18px;
  }
  .tab-bar {
    position: absolute; left: 23px; top: 31px; width: 434px; height: 89px;
    background: var(--tab-bg);
    display: flex; border-bottom: 7px solid var(--tab-track);
  }
  .tab {
    flex: 1; display: flex; align-items: center; justify-content: center;
    color: var(--tab-text); font-size: 17px;
    border-right: 1px solid var(--tab-divider); position: relative;
  }
  .tab:last-child { border-right: 0; }
  .tab.is-active::after {
    content: ""; position: absolute; left: 0; right: 0; bottom: -7px; height: 7px;
    background: var(--accent);
  }
  .action-button {
    position: absolute; top: 134px; height: 70px;
    background: linear-gradient(var(--button-top), var(--button-bottom));
    border: 1px solid var(--button-border); border-radius: 3px;
    color: #fff; font-family: "Montserrat", sans-serif; font-weight: 600;
    display: flex; flex-direction: column; align-items: center; justify-content: center;
    box-shadow: 0 2px 4px rgba(0,0,0,.5);
  }
  .quick-play { left: 30px; width: 205px; font-size: 20px; }
  .quick-play small { font-size: 9px; font-weight: 600; margin-top: 1px; }
  .challenge-friend { left: 245px; width: 205px; font-size: 20px; }
  .category-list { position: absolute; left: 23px; top: 224px; width: 434px; list-style: none; }
  .category {
    height: 87px; position: relative;
    background: linear-gradient(var(--row-top), var(--row-bottom));
    border-top: 1px solid var(--row-divider);
  }
  .category-name {
    position: absolute; left: 14px; bottom: 10px;
    font-family: "Montserrat", sans-serif; font-weight: 600; font-size: 17px;
    color: var(--row-title);
  }
  .category-stats {
    position: absolute; right: 14px; top: 6px; text-align: right;
    font-size: 14px; line-height: 17px; color: var(--row-meta);
  }
  .category-lock { position: absolute; right: 13px; bottom: 7px; }
</style>
</head>
<body>
  <main class="app-screen">
    <div class="status-bar">
      <div class="status-carrier">
        <svg width="28" height="14" viewBox="0 0 28 14" aria-hidden="true">
          <g fill="#e6e6e6"><rect x="0" y="10" width="4" height="4"/><rect x="6" y="8" width="4" height="6"/><rect x="12" y="6" width="4" height="8"/><rect x="18" y="3" width="4" height="11"/><rect x="24" y="0" width="4" height="14"/></g>
        </svg>
        CARRIER
      </div>
      <svg width="16" height="20" viewBox="0 0 16 20" aria-hidden="true">
        <path d="M4 9V6a4 4 0 0 1 8 0v3" fill="none" stroke="#cfcfcf" stroke-width="2.2"/>
        <rect x="1" y="9" width="14" height="11" rx="1" fill="#cfcfcf"/>
      </svg>
      <svg width="31" height="14" viewBox="0 0 31 14" aria-hidden="true">
        <rect x="1" y="1" width="26" height="12" rx="2" fill="none" stroke="#e6e6e6" stroke-width="1.5"/>
        <rect x="3" y="3" width="22" height="8" fill="#e6e6e6"/>
        <rect x="28" y="4.5" width="2.5" height="5" fill="#e6e6e6"/>
      </svg>
    </div>

    <nav class="tab-bar">
      <div class="tab is-active">Home</div>
      <div class="tab">Matches</div>
      <div class="tab">Rankings</div>
      <div class="tab">Settings</div>
    </nav>

    <div class="action-button quick-play">Quick Play<small>Vs Random</small></div>
    <div class="action-button challenge-friend">Challenge Friend</div>

    <ul class="category-list">
      <li class="category">
        <div class="category-stats">- 287, L1<br>- 1480</div>
        <span class="category-name">Lesendary Goalkeepers</span>
        <svg class="category-lock" width="26" height="34" viewBox="0 0 26 34" aria-hidden="true"><path d="M6 15V9a7 7 0 0 1 14 0v2" fill="none" stroke="var(--lock)" stroke-width="3.5"/><rect x="1" y="14" width="24" height="19" rx="3" fill="var(--lock)"/><circle cx="13" cy="22" r="3.2" fill="#d6d7d9"/><rect x="11.8" y="23" width="2.4" height="5.5" fill="#d6d7d9"/></svg>
      </li>
      <li class="category">
        <div class="category-stats">- 201 L1<br>- 940</div>
        <span class="category-name">Continental Cup</span>
        <svg class="category-lock" width="26" height="34" viewBox="0 0 26 34" aria-hidden="true"><path d="M6 15V9a7 7 0 0 1 14 0v6" fill="none" stroke="var(--lock)" stroke-width="3.5"/><rect x="1" y="14" width="24" height="19" rx="3" fill="var(--lock)"/><circle cx="13" cy="22" r="3.2" fill="#d6d7d9"/><rect x="11.8" y="23" width="2.4" height="5.5" fill="#d6d7d9"/></svg>
      </li>
      <li class="category">
        <div class="category-stats">- 441 L1<br>- 920</div>
        <span class="category-name">Nordliga</span>
        <svg class="category-lock" width="26" height="34" viewBox="0 0 26 34" aria-hidden="true"><path d="M6 15V9a7 7 0 0 1 14 0v6" fill="none" stroke="var(--lock)" stroke-width="3.5"/><rect x="1" y="14" width="24" height="19" rx="3" fill="var(--lock)"/><circle cx="13" cy="22" r="3.2" fill="#d6d7d9"/><rect x="11.8" y="23" width="2.4" height="5.5" fill="#d6d7d9"/></svg>
      </li>
      <li class="category">
        <div class="category-stats">- 120 L1<br>- 440</div>
        <span class="category-name">Calcio Top 2013/14</span>
        <svg class="category-lock" width="26" height="34" viewBox="0 0 26 34" aria-hidden="true"><path d="M6 15V9a7 7 0 0 1 14 0v6" fill="none" stroke="var(--lock)" stroke-width="3.5"/><rect x="1" y="14" width="24" height="19" rx="3" fill="var(--lock)"/><circle cx="13" cy="22" r="3.2" fill="#d6d7d9"/><rect x="11.8" y="23" width="2.4" height="5.5" fill="#d6d7d9"/></svg>
      </li>
      <li class="category">
        <div class="category-stats">- 370 L1<br>- 1240</div>
        <span class="category-name">Global Finals 1994</span>
        <svg class="category-lock" width="26" height="34" viewBox="0 0 26 34" aria-hidden="true"><path d="M6 15V9a7 7 0 0 1 14 0v2" fill="none" stroke="var(--lock)" stroke-width="3.5"/><rect x="1" y="14" width="24" height="19" rx="3" fill="var(--lock)"/><circle cx="13" cy="22" r="3.2" fill="#d6d7d9"/><rect x="11.8" y="23" width="2.4" height="5.5" fill="#d6d7d9"/></svg>
      </li>
      <li class="category">
        <div class="category-stats">- 410 L1<br>- 740</div>
        <span class="category-name">September 2013</span>
        <svg class="category-lock" width="26" height="34" viewBox="0 0 26 34" aria-hidden="true"><path d="M6 15V9a7 7 0 0 1 14 0v6" fill="none" stroke="var(--lock)" stroke-width="3.5"/><rect x="1" y="14" width="24" height="19" rx="3" fill="var(--lock)"/><circle cx="13" cy="22" r="3.2" fill="#d6d7d9"/><rect x="11.8" y="23" width="2.4" height="5.5" fill="#d6d7d9"/></svg>
      </li>
      <li class="category">
        <div class="category-stats">- 370 L1<br>- 1240</div>
        <span class="category-name">Global Finals 1994</span>
        <svg class="category-lock" width="26" height="34" viewBox="0 0 26 34" aria-hidden="true"><path d="M6 15V9a7 7 0 0 1 14 0v2" fill="none" stroke="var(--lock)" stroke-width="3.5"/><rect x="1" y="14" width="24" height="19" rx="3" fill="var(--lock)"/><circle cx="13" cy="22" r="3.2" fill="#d6d7d9"/><rect x="11.8" y="23" width="2.4" height="5.5" fill="#d6d7d9"/></svg>
      </li>
    </ul>
  </main>
</body>
</html>
```